Graphic to show easy steps to find financial clarity

Howdy-I need a graphic that describe my Coin Harbor Method.The attached is a concept, but please use your own creativity to show how you would display this:- There are 5 steps the process (and then we repeat/recalculate)- And three bullets that drive home the results of the processI've also attached my logo. Please use the colors in my logo and maybe add a soft green as needed.The reader should be able to briefly scan this document and understand that this is an easy/simple process that tells them how to manage their cash.Thanks!-Ned

Target Market(s)

wealthy women, whether single or married

Requirements
Must have
• Please use the colors in my logo and a soft green if needed
Should not have
• This should be a very easy to read graphic that communicates how simple/easy this is to do.

```html
<!DOCTYPE html>
<html lang="en">
<head>
<meta charset="utf-8">
<title>Coin Harbor Method</title>
<link rel="stylesheet" href="https://fonts.googleapis.com/css2?family=Nunito+Sans:wght@700;800;900&family=Playfair+Display:wght@400&display=swap">
<style>
  :root {
    --navy: #1f3b79;
    --sky: #1cb0e6;
    --slate: #545457;
    --mist: #e7e7e9;
    --repeat-text: #58585b;
    --white: #ffffff;
    --body-text: #4a4a4d;
  }
  html, body { margin: 0; padding: 0; overflow: hidden; background: var(--white); }
  .canvas {
    position: relative; width: 927px; height: 1200px; overflow: hidden;
    background: var(--white);
    font-family: "Nunito Sans", Arial, sans-serif;
  }
  .ring { position: absolute; left: 0; top: 0; }
  .brand {
    position: absolute; left: 660px; top: 48px;
    display: flex; align-items: center; gap: 10px;
  }
  .brand-mark { width: 34px; height: 34px; background: var(--navy); }
  .brand-name {
    font-family: "Playfair Display", Georgia, serif; font-size: 19px;
    color: var(--navy); line-height: 1.1; width: 190px;
  }
  .label {
    position: absolute; color: var(--white); font-weight: 800;
    font-size: 21px; line-height: 29px; letter-spacing: .2px;
  }
  .label.right { text-align: right; }
  .label.center { text-align: center; }
  .label.repeat-note { color: var(--repeat-text); }
  .step-tag {
    position: absolute; color: var(--navy); font-weight: 900; text-align: center;
    width: 60px;
  }
  .step-tag .word { font-size: 17px; line-height: 18px; display: block; letter-spacing: .5px; }
  .step-tag .num { font-size: 54px; line-height: 50px; display: block; }
  .step-tag.on-slate { color: var(--slate); }
  .repeat-word {
    position: absolute; left: 205px; top: 240px; font-weight: 900;
    font-size: 22px; color: var(--repeat-text); letter-spacing: .5px;
  }
  .title {
    position: absolute; left: 300px; top: 512px; width: 328px; text-align: center;
    font-family: "Playfair Display", Georgia, serif; font-size: 47px; line-height: 54px;
    color: #2a2a2c;
  }
  .result {
    position: absolute; top: 850px; width: 230px; text-align: center;
  }
  .result-icon { width: 134px; height: 134px; border-radius: 50%; margin: 0 auto; display: flex; align-items: center; justify-content: center; }
  .result h2 { margin: 8px 0 0; font-size: 46px; font-weight: 900; line-height: 56px; letter-spacing: .5px; }
  .result p { margin: 4px 0 0; font-size: 18px; font-weight: 700; line-height: 24px; color: var(--body-text); }
  .result.know { left: 104px; }
  .result.know .result-icon { background: var(--navy); }
  .result.know h2 { color: var(--navy); }
  .result.spend { left: 348px; }
  .result.spend .result-icon { background: var(--sky); }
  .result.spend h2 { color: var(--sky); }
  .result.create { left: 596px; }
  .result.create .result-icon { background: var(--slate); }
  .result.create h2 { color: var(--slate); }
  .joy-stamp {
    display: inline-block; margin-top: 8px; padding: 2px 12px;
    border: 4px solid var(--sky); border-radius: 4px; color: var(--sky);
    font-weight: 900; font-size: 32px; line-height: 40px; transform: rotate(-4deg);
  }
</style>
</head>
<body>
<div class="canvas">

  <svg class="ring" width="927" height="1200" viewBox="0 0 927 1200" aria-hidden="true">
    <g stroke="var(--white)" stroke-width="6">
      <path fill="var(--navy)"  d="M464 133 A346 346 0 0 1 763.6 306 L626.8 385 A188 188 0 0 0 464 291 Z"/>
      <path fill="var(--sky)"   d="M763.6 306 A346 346 0 0 1 763.6 652 L626.8 573 A188 188 0 0 0 626.8 385 Z"/>
      <path fill="var(--slate)" d="M763.6 652 A346 346 0 0 1 464 825 L464 667 A188 188 0 0 0 626.8 573 Z"/>
      <path fill="var(--navy)"  d="M464 825 A346 346 0 0 1 164.4 652 L301.2 573 A188 188 0 0 0 464 667 Z"/>
      <path fill="var(--sky)"   d="M164.4 652 A346 346 0 0 1 164.4 306 L301.2 385 A188 188 0 0 0 301.2 573 Z"/>
      <path fill="var(--mist)"  d="M164.4 306 A346 346 0 0 1 464 133 L464 291 A188 188 0 0 0 301.2 385 Z"/>
    </g>

    <!-- step tabs -->
    <g fill="var(--white)">
      <polygon points="472,150 553,150 575,188 553,226 472,226"/>
      <polygon points="630,390 703,390 725,430 703,470 630,470"/>
      <polygon points="472,704 553,704 575,742 553,780 472,780"/>
      <polygon points="198,646 275,646 297,686 275,726 198,726"/>
      <polygon points="120,360 213,360 235,400 213,440 120,440"/>
      <polygon points="176,226 312,226 334,260 312,294 176,294"/>
    </g>

    <!-- repeat arrows -->
    <g fill="none" stroke="#555" stroke-width="3" stroke-linecap="round">
      <path d="M150 248 C 200 140, 300 95, 428 92"/>
      <path d="M416 80 L430 92 L416 104"/>
      <path d="M303 345 C 330 300, 380 272, 428 268"/>
      <path d="M416 256 L430 268 L416 280"/>
    </g>

    <!-- center cycle icon -->
    <g fill="none" stroke-linecap="round">
      <circle cx="461" cy="430" r="30" stroke="var(--sky)" stroke-width="4"/>
      <circle cx="461" cy="430" r="20" stroke="var(--navy)" stroke-width="4"/>
      <path d="M423 370 C 400 372, 400 400, 410 420" stroke="var(--slate)" stroke-width="4"/>
      <path d="M499 490 C 522 488, 522 460, 512 440" stroke="var(--slate)" stroke-width="4"/>
      <path d="M492 372 C 520 390, 522 430, 506 465" stroke="var(--sky)" stroke-width="4"/>
      <path d="M480 362 L492 372 L480 384" stroke="var(--sky)" stroke-width="4"/>
      <path d="M430 488 C 402 470, 400 430, 416 395" stroke="var(--sky)" stroke-width="4"/>
      <path d="M442 498 L430 488 L442 476" stroke="var(--sky)" stroke-width="4"/>
    </g>
    <text x="461" y="439" text-anchor="middle" font-family="Nunito Sans, Arial, sans-serif" font-weight="900" font-size="24" fill="var(--navy)">$</text>
  </svg>

  <div class="brand">
    <div class="brand-mark"></div>
    <div class="brand-name">Tidewell Wealth Partners</div>
  </div>

  <div class="step-tag" style="left:482px;top:156px"><span class="word">STEP</span><span class="num">1</span></div>
  <div class="step-tag" style="left:638px;top:396px"><span class="word">STEP</span><span class="num">2</span></div>
  <div class="step-tag on-slate" style="left:482px;top:710px"><span class="word">STEP</span><span class="num">3</span></div>
  <div class="step-tag" style="left:206px;top:652px"><span class="word">STEP</span><span class="num">4</span></div>
  <div class="step-tag" style="left:140px;top:366px"><span class="word">STEP</span><span class="num">5</span></div>
  <div class="repeat-word">REPEAT</div>

  <div class="label right repeat-note" style="left:268px;top:180px;width:176px">Recalculate<br>monthly</div>
  <div class="label right" style="left:540px;top:220px;width:142px">Know<br>your annual<br>spending</div>
  <div class="label center" style="left:650px;top:487px;width:150px">Project<br>special<br>expenses</div>
  <div class="label right" style="left:520px;top:646px;width:182px">Add up your<br>5-year cash<br>needs</div>
  <div class="label right" style="left:300px;top:684px;width:140px">Set them<br>aside in<br>savings</div>
  <div class="label center" style="left:148px;top:481px;width:112px">Invest<br>the rest</div>

  <div class="title">Coin Harbor<br>Method</div>

  <div class="result know">
    <div class="result-icon">
      <svg width="70" height="60" viewBox="0 0 70 60" fill="none" stroke="var(--white)" stroke-width="3" stroke-linejoin="round" aria-hidden="true">
        <path d="M15 10 H55 L66 24 L35 56 L4 24 Z"/><path d="M4 24 H66 M25 10 L20 24 L35 56 L50 24 L45 10"/>
      </svg>
    </div>
    <h2>KNOW</h2>
    <p>your lifestyle will be unaffected by the markets for at least 5 years</p>
  </div>

  <div class="result spend">
    <div class="result-icon">
      <svg width="70" height="66" viewBox="0 0 70 66" fill="none" stroke="var(--white)" stroke-width="3" stroke-linejoin="round" aria-hidden="true">
        <rect x="26" y="14" width="38" height="48"/><path d="M36 14 V8 a9 9 0 0 1 18 0 V14"/>
        <rect x="4" y="36" width="30" height="26"/><path d="M4 44 H34 M19 36 V62 M19 36 C12 26, 8 34, 19 36 C26 26, 30 34, 19 36"/>
      </svg>
    </div>
    <h2>SPEND</h2>
    <p>intentionally and with</p>
    <span class="joy-stamp">JOY</span>
  </div>

  <div class="result create">
    <div class="result-icon">
      <svg width="70" height="66" viewBox="0 0 70 66" fill="none" stroke="var(--white)" stroke-width="3" aria-hidden="true">
        <path d="M6 10 H40 M6 18 H40 M6 26 H40 M6 34 H30 M6 42 H28 M6 50 H30 M6 58 H36"/>
        <circle cx="48" cy="44" r="18"/><circle cx="48" cy="44" r="12"/>
        <text x="48" y="50" text-anchor="middle" font-family="Nunito Sans, Arial, sans-serif" font-size="16" font-weight="900" fill="var(--white)" stroke="none">$</text>
      </svg>
    </div>
    <h2>CREATE</h2>
    <p>a solid base for lifetime cash flow projections</p>
  </div>

</div>
</body>
</html>
```